Design einer Frühjahrsbroschüre für Immobilienmakler
Zielgruppe
Wir sind Immobilienmakler und möchten eine neue Frühjahrsbroschüre verteilen lassen.
Wir haben über Gestaltfinder schon mehrere Projekte gemacht und waren immer zufrieden.
Unsere Zielgruppe sind Immobilienverkäufer.
Aufgabenstellung
Der Flyer soll die Größe haben DinA3 auf DinA4 gefaltet. Somit sind 4 DinA4 Seiten zu gestallten.
Bei Papier zum Glück soll gedruckt werden. https://www.papier-zum-glueck.de/faltblatt-gefalzt-auf-din-a4-4seiter.html#content-view
1. Seite: Frühlingshaft und ansprechende Aufmachung. Harmonische Farben. Ein Slogan.
Frühjahrsaktion: Verkäufer erhält nach Verkauf als Dankeschön für den Auftrag und sein Vertrauen in uns einen neuen Kochwunder KX8 oder 1000€ in bar.
2. Immobilienverkauf in Coronazeiten.
Warum Verkaufen mit Nord-Immobilien Kleebach
3. Aktuelle Immobilienangebote
4. Wir suchen für unsere Kunden
Im Anhang sind andere Flyer/Broschüren die uns seither gut gefallen haben.

```html
<!DOCTYPE html>
<html lang="de">
<head>
<meta charset="utf-8">
<title>Nord-Immobilien Kleebach – Frühjahrsbroschüre Innenseiten</title>
<link href="https://fonts.googleapis.com/css2?family=Overpass:wght@400;600;800;900&display=swap" rel="stylesheet">
<style>
  :root{
    --navy:#1d3d6e;
    --gold:#b8923f;
    --paper:#ffffff;
    --ink:#1d3d6e;
  }
  *{box-sizing:border-box;margin:0;padding:0}
  html,body{width:1200px;height:849px;overflow:hidden;background:var(--paper)}
  body{font-family:"Overpass",Arial,sans-serif;color:var(--ink)}
  .spread{position:relative;width:1200px;height:849px;background:var(--paper)}
  .fold{position:absolute;left:593px;top:0;width:2px;height:849px;background:var(--navy)}

  .frame{position:absolute;border:3px solid var(--gold)}
  .brand-mark{position:absolute;display:flex;align-items:center;gap:6px;
    font-weight:800;font-size:11px;color:var(--navy);letter-spacing:.02em;white-space:nowrap}
  .brand-mark .dot{width:18px;height:18px;border-radius:50%;background:var(--navy)}

  .photo{position:absolute}
  .photo-label{position:absolute;color:#fff;font-weight:900;font-size:14px;line-height:16px;letter-spacing:.08em}

  /* left page */
  .intro-frame{left:-3px;top:80px;width:306px;height:153px;border-left:none}
  .intro-title{position:absolute;left:35px;top:118px;width:260px}
  .intro-title h1{font-weight:900;font-size:19.5px;line-height:21px;letter-spacing:.03em;text-transform:uppercase}
  .intro-title p{font-size:18px;line-height:22px;font-weight:400}
  .body-col{position:absolute;top:296px;width:250px;font-size:10.6px;line-height:14.3px}
  .body-col p{margin-bottom:14.3px}
  .body-col b{font-weight:800}
  .col-a{left:36px}
  .col-b{left:296px}
  .footer-block{position:absolute;top:736px;font-size:14px;line-height:17px}
  .footer-block h2{font-weight:900;font-size:14px;letter-spacing:.05em;text-transform:uppercase}
  .footer-block .gold{color:var(--gold);font-weight:600}
  .foot-a{left:36px}
  .foot-b{left:296px}

  /* right page */
  .offers-frame{left:930px;top:80px;width:220px;height:129px}
  .offers-title{position:absolute;left:976px;top:117px;font-weight:900;font-size:19.5px;line-height:21.5px;letter-spacing:.04em}
  .object-frame{left:629px;top:36px;width:257px;height:300px;border-right:none;border-bottom:none}
  .side{position:absolute;left:1020px;top:418px;width:160px;font-size:10.8px;line-height:13.4px}
  .side h3{font-weight:900;font-size:10.8px;letter-spacing:.03em;text-transform:uppercase}
  .side .sub{font-weight:800;font-size:10.8px}
  .side p{margin-bottom:12px}
  .callout{position:absolute;left:660px;top:464px;font-weight:800;font-size:10px;line-height:12px;color:var(--navy)}
</style>
</head>
<body>
<main class="spread">

  <!-- Left page: selling in corona times -->
  <section class="page page-left">
    <div class="brand-mark" style="left:108px;top:52px"><span class="dot"></span>Nord-Immobilien Kleebach</div>
    <div class="frame intro-frame"></div>
    <div class="intro-title">
      <h1>Immobilienverkauf in Coronazeiten.</h1>
      <p>Warum Verkaufen mit Nord-Immobilien Kleebach?</p>
    </div>
    <div class="photo" role="img" aria-label="Luftaufnahme einer Wohnsiedlung mit Mehrfamilienhäusern und Gewerbegebiet im Hintergrund"
         style="left:330px;top:80px;width:226px;height:153px;background:linear-gradient(180deg,#bcc8d6 0%,#a7b08e 22%,#8c8f72 50%,#9c7a62 75%,#7f8a64 100%)"></div>

    <div class="body-col col-a">
      <p>Sie fragen sich ob es gerade jetzt – mitten in der <b>Corona-Krise</b> – ein guter Zeitpunkt für den Immobilienverkauf ist? Wie kann man dies mit den aktuellen Corona-Vorschriften vereinbaren? Welcher Verkaufspreis lässt sich erzielen?</p>
      <p>Diese und viele weitere Fragen beantworten wir Ihnen im Rahmen einer <b>unverbindlichen Beratung.</b> Gerne per Telefon oder Videokonferenz. Ist Ihnen eine persönliche Beratung lieber?</p>
      <p>Dann machen wir auch dies möglich wenn es gewährleistet ist dass man den Mindestabstand von 1,5 m einhalten kann. Gerne halten wir die Gespräche auch im Freien wie im Garten oder auf dem Balkon ab. Natürlich kommen wir immer mit Mundschutz und Handschuhen.</p>
      <p>Nach unserer Beratung und einer <b>unverbindlichen und kostenlosen Objektbewertung</b> haben Sie eine fundierte Grundlage um zu entscheiden ob ein Verkauf für Sie in Frage kommt.</p>
      <p>Haben Sie sich zum Verkauf Ihrer Immobilie mit uns entschieden machen wir ansprechende, professionelle Fotos und erstellen ein attraktives Exposé welche Sie per Mail vorab erhalten und</p>
    </div>
    <div class="body-col col-b">
      <p>freigeben können. Der Fototermin findet selbstverständlich auch unter Einhaltung der Hygienemaßnahmen statt.</p>
      <p>Wir bewerben Ihre Immobilie auf Portalen wie Wohnportal24, Marktplatz Kleinanzeigen, Nachbarnetz und auf unserer Homepage. Darüber hinaus ermitteln wir passende Kaufinteressenten aus unserer Datenbank.</p>
      <p>Um Ihre Immobilie auch in diesen Zeiten erfolgreich zu verkaufen, haben wir auch für Ihre Kaufinteressenten digitale Lösungen geschaffen. Sollte ein Vor-Ort-Termin (mit max. 2 Personen) nicht möglich sein, besteht auch hier die Möglichkeit Ihre Immobilie in Videokonferenzen und Video-Besichtigungstouren zu präsentieren.</p>
      <p>Käufer und Kaufpreis passen für Sie? Dann kümmern wir uns um den Kaufvertrag und den Notartermin, um den Verkauf rechtssicher abzuschließen.</p>
      <p><b>Übrigens:</b> In den letzten zwei Jahren waren 93 Prozent unserer Kunden mit unserem Service, der Vermarktungsdauer und dem erzielten Preis sehr zufrieden.</p>
    </div>

    <div class="footer-block foot-a">
      <h2>Wir verkaufen<br>Ihre Immobilie richtig</h2>
      <div class="gold">Professionell, zeitnah/schnell,<br>fair und kostengünstig</div>
    </div>
    <div class="footer-block foot-b">
      <h2>Mehr erfahren:</h2>
      <div class="gold">www.nordimmo-kleebach.de</div>
      <h2>Kontakt:</h2>
      <div class="gold">info@nordimmo-kleebach.de</div>
    </div>
  </section>

  <div class="fold"></div>

  <!-- Right page: current offers -->
  <section class="page page-right">
    <div class="frame object-frame"></div>
    <div class="photo" role="img" aria-label="Langgestreckte Halle mit dunkler Holzfassade und Glasfenstern über einer Wiese"
         style="left:640px;top:47px;width:263px;height:300px;background:linear-gradient(180deg,#6f5a4a 0%,#3e3530 30%,#7d8576 55%,#86a05a 75%,#5f7d3c 100%)">
      <div class="photo-label" style="left:28px;top:252px">TITEL<br>OBJEKT</div>
    </div>
    <div class="photo" role="img" aria-label="Einfamilienhaus mit Solardach und Garten mit Felsen und Sträuchern"
         style="left:875px;top:235px;width:276px;height:157px;background:linear-gradient(180deg,#4f86d6 0%,#a9c2e6 35%,#9c8c74 55%,#6d8a44 78%,#4c6a2c 100%)">
      <div class="photo-label" style="left:200px;top:112px">TITEL<br>OBJEKT</div>
    </div>

    <div class="brand-mark" style="left:980px;top:52px"><span class="dot"></span>Nord-Immobilien Kleebach</div>
    <div class="frame offers-frame"></div>
    <div class="offers-title">AKTUELLE<br>IMMOBILIEN-<br>ANGEBOTE</div>

    <div class="photo" role="img" aria-label="Weißes Wohn- und Geschäftshaus mit rotem Ziegeldach unter blauem Himmel"
         style="left:595px;top:420px;width:393px;height:383px;background:linear-gradient(180deg,#7fa8dc 0%,#a8c4e4 40%,#e6e7e6 62%,#d9d9d6 80%,#a77a6c 92%,#8f7468 100%)">
      <svg width="393" height="383" style="position:absolute;left:0;top:0" aria-hidden="true">
        <rect x="125" y="18" width="254" height="339" fill="none" stroke="#1d3d6e" stroke-width="1"/>
        <rect x="132" y="24" width="241" height="327" fill="none" stroke="#ffffff" stroke-width="1"/>
        <line x1="120" y1="60" x2="210" y2="60" stroke="#1d3d6e" stroke-width="1.2"/>
      </svg>
      <div class="photo-label" style="left:30px;top:338px">TITEL<br>OBJEKT</div>
    </div>
    <div class="callout">zu ver-<br>kaufender<br>Gebäudeteil</div>

    <aside class="side">
      <p><h3>Warum mit<br>Nord-Immobilien<br>verkaufen?</h3>Unser Versprechen: 100% Maklerservice, 0% Provisionsschmerz</p>
      <p><span class="sub">Erfahrene Makler</span><br>Wir kommen aus der Region und kennen den lokalen Immobilienmarkt seit Jahren.</p>
      <p><span class="sub">Volle Serviceleistung</span><br>Ihr lokaler Makler steht Ihnen bei jedem Schritt des Verkaufs zur Seite: von der Bewertung und Bewerbung bis zur Schlüsselübergabe.</p>
      <p><span class="sub">Keine Verkaufsprovision</span><br>Der gesamte Service ist bei uns für Verkäufer kostenfrei.</p>
      <p>Auch Käufer zahlen weniger Provision als marktüblich.</p>
    </aside>
  </section>

</main>
</body>
</html>
```